Recruitment Consulting Business Card Design

I require a business card design for my company which is based in Sydney, Australia called Velmora Consulting Group. My company specializes in assisting hotels/resorts across Australia in finding suitable candidates to meet their recruitment needs in the frontline hospitality space. In terms of the candidates I utilise, they are sourced from working holiday visa makers to Australia deriving from Japan, Korea, Taiwan and Hong Kong primarily. The main purpose of the business is to connect both hotels/resorts and individuals together. On one side - hotels/resorts are looking for skilled and willing individuals to work for them, whilst candidates are looking for opportunities to work, make some money, obtain job skills whilst they are living in Australia.

The name of the company Velmora can be looked at as either one word or as two words. It can be abbreviated to Tallow Brook. In essence I view my business as one that connects/brings people and organizations together to mutual benefit.

For my design I would like to see designs that utilze the colors blue, dark blue, silver and white. The logo is the most difficult thing I find to put together as I dont have access to different fonts. You could accentuate on the P in Velmora in designing the logo.

The brand itself should communicate interconnectedness, creativity, innovation and inspiration. I had used those terms Innovate Create Inspire in my original logo which I designed.

Hi there.

I forgot to add in all my details for the card.  The details as follows:

Gareth M Olsen
Director

Suite 8, Level 6
Elm Court, 2-6 Harwick Lane
Chatswood, NSW, 2067
Australia

Mobile: +61 455 727 916
Telephone: +61 2 9736 2045
Email: gareth@velmoraconsulting.com.au

Also, I would like to try designs with a darker navy blue. 

Reason: I have decided to extend the deadline for this project. I thank you all for your designs so far and a few of them are under heavy consideration. Despite the fact that I have provided previous art work for my logo I am looking for someone to put forth an idea for a new logo to be incorporated into the business card. Thank you again for all your hard work and look forward to a further influx of designs. Gareth

Hi All,

QuillHarborStudio is the front runner for the card design. I have attached his image to give you a better idea of where I am at with my decisions.  

Generally speaking we like his design cause it is:

Clean looking 
Modern
Sophisticated, Simple but Professional Looking
Good use of multi colours on the back of the card.

Only thing I am looking to change is to make a new logo and not use the P
I am looking for a circle type logo such as that used by Venthaux in the attachments I have uploaded. Utilizing silver, blue (can try different shades) and silver.

I look forward to more designs and for those that put more effort in at this point I am willing to consider paying extra.

Thank you

Kind Regards,

Gareth

Reason: Extremely busy time at work and I havent had time to review or provide proper feedback. Some great designs out there and decision will be forthcoming at the end of this week.

Target Market(s)

Hotels and Resorts

Industry/Entity Type

Hospitality

Contact Information for Business Card

Gareth M Olsen
Director
Velmora Consulting Group
Suite 8, Level 6, Elm Court, 2-6 Harwick Lane,
Chatswood, NSW, 2067, Australia

Logo Text

Velmora for the main logo with subtext taglines - Create, Innovate, Inspire

Logo styles of interest
Abstract Logo
Wordmark Logo
Requirements
Must have
• A bold but warm design for the word Velmora

Could put the taglines at the bottom - Innovate, Create, Inspire

Keep the business logo clean but sophisticated
Nice to have
• The word Velmora embossed or brought forward and out with silver lines behind the word and logo creating a sense of motion or lines at the left and right of the word Velmora which provides the notion of connecting people/organizations together.

```html
<!DOCTYPE html>
<html lang="en">
<head>
<meta charset="utf-8">
<title>Velmora Consulting – Business Card</title>
<link rel="stylesheet" href="https://fonts.googleapis.com/css2?family=Source+Sans+3:wght@400;600;700&display=swap">
<style>
  :root {
    --brand-blue: #2f6a9c;
    --brand-navy: #2b5a85;
    --silver: #8a8d91;
    --rule: #b9bbbe;
    --card-edge: #d6d6d6;
    --paper: #ffffff;
    --canvas: #ffffff;
  }
  * { box-sizing: border-box; margin: 0; padding: 0; }
  html, body {
    width: 1200px; height: 1000px; overflow: hidden;
    background: var(--canvas);
    font-family: "Source Sans 3", "Myriad Pro", Arial, sans-serif;
  }
  .stage { position: relative; width: 1200px; height: 1000px; }
  .card {
    position: absolute;
    background: var(--paper);
    border: 1px solid var(--card-edge);
    box-shadow: 5px 6px 8px rgba(0,0,0,0.22);
  }
  .card--front { left: 232px; top: 43px; width: 738px; height: 415px; }
  .card--back  { left: 241px; top: 502px; width: 739px; height: 414px; }

  /* front */
  .front-mark {
    position: absolute; left: 333px; top: 130px;
    width: 70px; height: 70px; border-radius: 50%;
    background: var(--brand-blue);
  }
  .front-wordmark {
    position: absolute; left: 0; right: 0; top: 210px;
    text-align: center; color: var(--brand-navy); font-weight: 700;
    line-height: 1;
  }
  .front-wordmark .name { display: block; font-size: 40px; letter-spacing: 3px; text-transform: uppercase; }
  .front-wordmark .sub { display: block; font-size: 17px; letter-spacing: 1px; margin-top: 6px; }
  .tagline {
    position: absolute; left: 0; right: 0; top: 322px;
    display: flex; justify-content: center; align-items: center;
    color: var(--brand-navy); font-size: 15px; font-weight: 600;
    letter-spacing: 4px;
  }
  .tagline .divider { width: 1px; height: 22px; background: var(--silver); margin: 0 26px; }

  /* back */
  .person { position: absolute; left: 30px; top: 34px; }
  .person__name { color: var(--brand-blue); font-size: 25px; font-weight: 700; line-height: 1.1; }
  .person__title { color: var(--silver); font-size: 14px; font-weight: 600; margin-top: 3px; }
  .back-wordmark {
    position: absolute; right: 30px; top: 36px; text-align: right;
    color: var(--brand-navy); font-weight: 700; line-height: 1;
  }
  .back-wordmark .name { display: block; font-size: 24px; letter-spacing: 2px; text-transform: uppercase; }
  .back-wordmark .sub { display: block; font-size: 15px; letter-spacing: 1px; margin-top: 3px; }
  .address {
    position: absolute; left: 30px; top: 151px;
    color: var(--brand-blue); font-size: 20px; line-height: 28px; font-style: normal;
  }
  .back-mark {
    position: absolute; left: 548px; top: 172px;
    width: 110px; height: 110px; border-radius: 50%;
    background: var(--brand-blue);
  }
  .rule { position: absolute; left: 24px; right: 24px; top: 309px; height: 1px; background: var(--rule); }
  .contact {
    position: absolute; display: flex; align-items: center; gap: 10px;
    color: var(--brand-blue); font-size: 19px;
  }
  .contact svg { width: 24px; height: 24px; flex: none; }
  .contact--phone  { left: 30px; top: 330px; }
  .contact--mobile { left: 30px; top: 368px; }
  .contact--email  { right: 28px; top: 330px; }
</style>
</head>
<body>
<main class="stage">
  <section class="card card--front" aria-label="Card front">
    <div class="front-mark"></div>
    <div class="front-wordmark">
      <span class="name">Velmora</span>
      <span class="sub">Consulting</span>
    </div>
    <div class="tagline">
      <span>Innovate</span><span class="divider"></span>
      <span>Create</span><span class="divider"></span>
      <span>Inspire</span>
    </div>
  </section>

  <section class="card card--back" aria-label="Card back">
    <div class="person">
      <div class="person__name">Mina Harlow</div>
      <div class="person__title">HR Operations / Training Coordinator</div>
    </div>
    <div class="back-wordmark">
      <span class="name">Velmora</span>
      <span class="sub">Consulting</span>
    </div>
    <address class="address">
      Suite 8, Level 6<br>
      Elm Court, 2-6 Harwick Lane<br>
      Chatswood, NSW, 2067<br>
      Australia
    </address>
    <div class="back-mark"></div>
    <div class="rule"></div>

    <div class="contact contact--phone">
      <svg viewBox="0 0 24 24" aria-hidden="true">
        <circle cx="12" cy="12" r="12" fill="var(--brand-navy)"/>
        <path d="M8.2 6.3c.5-.4 1.2-.3 1.5.2l1.2 1.9c.3.5.2 1.1-.2 1.4l-.8.6c.6 1.4 1.7 2.6 3.1 3.3l.7-.8c.4-.4 1-.5 1.4-.2l1.9 1.2c.5.3.6 1 .2 1.5l-.9 1c-.7.7-1.8.9-2.7.5-3-1.3-5.3-3.7-6.5-6.7-.4-.9-.2-2 .5-2.7z" fill="#fff"/>
      </svg>
      <span>+61 2 9736 2045</span>
    </div>
    <div class="contact contact--mobile">
      <svg viewBox="0 0 24 24" aria-hidden="true">
        <circle cx="12" cy="12" r="12" fill="var(--brand-navy)"/>
        <rect x="8.5" y="5.5" width="7" height="13" rx="1.3" fill="none" stroke="#fff" stroke-width="1.6"/>
        <circle cx="12" cy="16.3" r=".9" fill="#fff"/>
      </svg>
      <span>+61 478 310 562</span>
    </div>
    <div class="contact contact--email">
      <svg viewBox="0 0 24 24" aria-hidden="true">
        <circle cx="12" cy="12" r="12" fill="var(--brand-navy)"/>
        <rect x="6" y="8" width="12" height="8.5" rx="1" fill="#fff"/>
        <path d="M6.5 8.6l5.5 4.3 5.5-4.3" fill="none" stroke="var(--brand-navy)" stroke-width="1.2"/>
      </svg>
      <span>mina@velmoraconsulting.com.au</span>
    </div>
  </section>
</main>
</body>
</html>
```